Business Card Design/Logo

I require a design/logo for my own Company, Morvix. The Jewellery I make is totally hand crafted. I own a hand Mining Claim out in the gemfields of Queensland and dig up my own stones. I also fossick for Gold Locally so all my Jewellery products are hand dug/cut/created. Quality stones are hand cut by my partner (Faceted) and other stones (Seconds) are either skin polished or recessed into pieces of Solid 925 Silver or Solid 9ct and 18 ct Gold. I make Sets (Collections) or just one-of designs. All the stones come in different colours and I am now starting to use different colour Golds. The final design should radiate professionalism, quality and uniqueness.

Target Market(s)

Many designs will cost a minimum of AU Dollars $2,000

Industry/Entity Type

Business

Contact Information for Business Card

Morvix Creations
Distinct Bench Wrought Native Adornments
0400327986
P.O. Box 418 Ambercrest 4719 Qld
morvixgarnets@mailbrook.net

```html
<!DOCTYPE html>
<html lang="en">
<head>
<meta charset="utf-8">
<title>Morvix Creations – Business Cards</title>
<link href="https://fonts.googleapis.com/css2?family=Source+Sans+3:wght@400;700&display=swap" rel="stylesheet">
<style>
  :root {
    --page: #ffffff;
    --onyx: #050505;
    --onyx-edge: #1a1a1a;
    --silver-light: #f4f4f4;
    --silver-mid: #c9c9c9;
    --silver-dark: #8e8e8e;
    --ink-light: #ffffff;
    --ink-soft: #e6e6e6;
    --ink-dark: #111111;
    --ink-grey: #2a2a2a;
    --ring-light: #eeeeee;
    --ring-mid: #a9adb3;
    --ring-dark: #4a4e55;
  }
  * { box-sizing: border-box; margin: 0; padding: 0; }
  html, body {
    width: 1200px;
    height: 1200px;
    overflow: hidden;
    background: var(--page);
    font-family: "Source Sans 3", "Myriad Pro", Arial, sans-serif;
  }
  .canvas {
    position: relative;
    width: 1200px;
    height: 1200px;
  }
  .card {
    position: absolute;
    left: 100px;
    width: 1000px;
    height: 560px;
    overflow: hidden;
    box-shadow: 0 6px 18px rgba(0,0,0,0.35);
  }
  .card--onyx {
    top: 30px;
    background: radial-gradient(ellipse at 70% 40%, var(--onyx-edge) 0%, var(--onyx) 60%);
    color: var(--ink-light);
  }
  .card--silver {
    top: 610px;
    background: linear-gradient(125deg, var(--silver-light) 0%, var(--silver-mid) 55%, var(--silver-dark) 100%);
    color: var(--ink-dark);
  }
  .ring-photo {
    position: absolute;
    width: 190px;
    height: 170px;
    border-radius: 50% 50% 44% 44%;
    background: radial-gradient(circle at 50% 42%, var(--ring-light) 0%, var(--ring-mid) 45%, var(--ring-dark) 100%);
  }
  .card--onyx .ring-photo { left: 150px; top: 70px; }
  .card--silver .ring-photo { left: 400px; top: 30px; }
  .brand-name {
    position: absolute;
    font-weight: 700;
    font-size: 80px;
    line-height: 1;
    letter-spacing: 1px;
    white-space: nowrap;
  }
  .card--onyx .brand-name--top { left: 560px; top: 70px; }
  .card--onyx .brand-name--bottom { left: 280px; top: 350px; }
  .card--silver .brand-name--left { left: 110px; top: 220px; }
  .card--silver .brand-name--right { left: 620px; top: 220px; }
  .contact {
    position: absolute;
    font-style: normal;
    font-size: 22px;
    line-height: 1.25;
    font-weight: 400;
    white-space: nowrap;
  }
  .card--onyx .contact { left: 590px; top: 330px; color: var(--ink-soft); }
  .card--silver .contact { left: 340px; top: 380px; color: var(--ink-grey); }
</style>
</head>
<body>
<main class="canvas">
  <section class="card card--onyx" aria-label="Business card, black face">
    <div class="ring-photo" role="img" aria-label="Photograph of a handmade silver ring with a large faceted stone"></div>
    <div class="brand-name brand-name--top">Morvix</div>
    <div class="brand-name brand-name--bottom">Morvix</div>
    <address class="contact">
      Morvix Creations Distinct Bench Wrought<br>
      Native Adornments 0400327986<br>
      P.O. Box 418 Ambercrest 4719<br>
      Email: Qld morvixgarnets@mailbrook.net
    </address>
  </section>

  <section class="card card--silver" aria-label="Business card, silver face">
    <div class="ring-photo" role="img" aria-label="Photograph of a handmade silver ring with a large faceted stone"></div>
    <div class="brand-name brand-name--left">Morvix</div>
    <div class="brand-name brand-name--right">Morvix</div>
    <address class="contact">
      Morvix Creations Distinct Bench Wrought<br>
      Native Adornments 0400327986<br>
      P.O. Box 418 Ambercrest 4719<br>
      Email: Qld morvixgarnets@mailbrook.net
    </address>
  </section>
</main>
</body>
</html>
```